Brightvale NA website
bright vale better days
Brightvale NA website - Energy
Creative Brief
Energy
We are a young company dedicate in energy saving and efficiency for cities, buildings and homes, to make a smarter and safer environment for city dwellers. We specialized in LED street lighting, LED commercial building with controlled systems for energy saving and smart home animation for lighting, thermo, alarm and all other electronics. You will have full control with your energy use remotely. We are targeting at government officials, new building management team, home owners. We offer LED lighting (interior and exterior), controlling system, user friendly software and home animation systems.
Like: Simple, brighter color theme, less wording more symbology and graphics Dislikes: too busy, too many words
light blue
light green
light orange
https://shop.hearthly-example.com/?ref=QwPlx7ZkTrmVbn4sYdHaJuEoGc
https://www.quorvel.com/
http://www.mellowbrew.com/
rainnie13 rainnie13
Thank you all for participating and the hard work, you guys have done a fantastic job in web design. 1. Please change the home animation into home automation. Thanks! 2. Please do not put too much information on the front page try to make it as simple as possible. 3. You guys have excellent choice of pictures just do find more symbols instead of small pictures for sections illustration. 4. Theme color do not use too many color just choose one I look forward to see more brilliant designs in the coming days! YOU ROCK!
Please use the logo on this website: www.brightvalena.com Thank you very much!
jogdesigner jogdesigner
Hello Project holder pls provide your logo to be used for the webdesign thank you

```html
<!DOCTYPE html>
<html lang="en">
<head>
<meta charset="utf-8">
<title>Brightvale NA</title>
<link href="https://fonts.googleapis.com/css2?family=Cinzel:wght@400;600;700&family=Lato:wght@400;700&display=swap" rel="stylesheet">
<style>
  :root {
    --accent: #f0782c;
    --ink: #333333;
    --nav: #4a4a4a;
    --band: #232323;
    --footer: #0d0d0d;
    --white: #ffffff;
    --social: #5b7fa8;
  }
  * { margin: 0; padding: 0; box-sizing: border-box; }
  html, body { width: 1200px; height: 978px; overflow: hidden; background: var(--white); }
  body { position: relative; font-family: "Lato", Arial, sans-serif; color: var(--ink); }

  .site-header { position: absolute; left: 0; top: 0; width: 1200px; height: 122px; background: var(--white); }
  .brand { position: absolute; left: 137px; top: 44px; font-size: 40px; font-weight: 700; color: var(--accent); letter-spacing: -0.5px; line-height: 1; }
  .social { position: absolute; left: 719px; top: 21px; display: flex; gap: 8px; }
  .social span { width: 40px; height: 40px; background: var(--social); display: block; }
  .header-phone { position: absolute; left: 930px; top: 28px; display: flex; align-items: center; gap: 10px; font-size: 18px; color: var(--nav); }
  .main-nav { position: absolute; left: 528px; top: 80px; display: flex; gap: 52px; }
  .main-nav a { font-size: 15px; color: var(--nav); text-decoration: none; letter-spacing: 0.5px; padding-bottom: 6px; }
  .main-nav a.current { color: var(--accent); border-bottom: 2px solid var(--accent); }

  .hero { position: absolute; left: 0; top: 122px; width: 1200px; height: 663px;
    background: linear-gradient(180deg, #1c2f8a 0%, #3a3fa6 35%, #6b4fa8 60%, #b0624e 82%, #e08a3a 100%); }
  .hero-title { position: absolute; left: 137px; top: 62px; font-family: "Cinzel", Georgia, serif; font-size: 40px; line-height: 54px; color: var(--white); font-weight: 600; }
  .slider-arrow { position: absolute; top: 338px; width: 27px; height: 27px; background: rgba(255,255,255,0.55); display: flex; align-items: center; justify-content: center; }
  .slider-arrow.prev { left: 105px; }
  .slider-arrow.next { left: 1065px; }

  .sectors { position: absolute; left: 0; top: 785px; width: 1200px; height: 145px; background: var(--band); }
  .sector { position: absolute; top: -61px; width: 200px; margin-left: -100px; text-align: center; }
  .sector-badge { width: 122px; height: 122px; border-radius: 50%; background: var(--white); border: 8px solid var(--accent); margin: 0 auto; display: flex; align-items: center; justify-content: center; }
  .sector-name { margin-top: 18px; font-size: 21px; font-weight: 700; color: var(--white); }

  .site-footer { position: absolute; left: 0; top: 930px; width: 1200px; height: 48px; background: var(--footer); color: var(--white); font-size: 13px; }
  .site-footer .item { position: absolute; top: 16px; display: flex; align-items: center; gap: 8px; }
  .newsletter { position: absolute; left: 820px; top: 7px; width: 172px; height: 34px; background: var(--white); color: #555; font-size: 12px; padding: 10px 8px; }
</style>
</head>
<body>
  <header class="site-header">
    <div class="brand">Brightvale NA</div>
    <div class="social"><span></span><span></span><span></span><span></span></div>
    <div class="header-phone">
      <svg width="20" height="20" viewBox="0 0 24 24"><circle cx="12" cy="12" r="11" fill="none" stroke="#f0782c" stroke-width="2"/><path d="M8 6l2 3-1.5 1.5a9 9 0 0 0 5 5L15 14l3 2-1 2c-5 0-10-5-10-10z" fill="#f0782c"/></svg>
      0987 604 215
    </div>
    <nav class="main-nav">
      <a class="current" href="#">HOME</a>
      <a href="#">ABOUT US</a>
      <a href="#">PRODUCTS</a>
      <a href="#">SERVICES</a>
      <a href="#">CONTACT US</a>
    </nav>
  </header>

  <section class="hero" role="img" aria-label="Night photo of a modern glass-and-steel building lit in blue, purple and warm lights under a dusk sky">
    <h1 class="hero-title">Lorem ipsum dolor sit<br>amet consecte</h1>
    <div class="slider-arrow prev"><svg width="12" height="14" viewBox="0 0 12 14"><path d="M9 1L3 7l6 6" fill="none" stroke="#333" stroke-width="2"/></svg></div>
    <div class="slider-arrow next"><svg width="12" height="14" viewBox="0 0 12 14"><path d="M3 1l6 6-6 6" fill="none" stroke="#333" stroke-width="2"/></svg></div>
  </section>

  <section class="sectors">
    <div class="sector" style="left:309px">
      <div class="sector-badge">
        <svg width="56" height="56" viewBox="0 0 56 56" fill="#111"><path d="M28 4L4 16v4h48v-4z"/><rect x="8" y="23" width="6" height="22"/><rect x="19" y="23" width="6" height="22"/><rect x="31" y="23" width="6" height="22"/><rect x="42" y="23" width="6" height="22"/><rect x="4" y="47" width="48" height="5"/></svg>
      </div>
      <div class="sector-name">Municipal</div>
    </div>
    <div class="sector" style="left:507px">
      <div class="sector-badge">
        <svg width="56" height="56" viewBox="0 0 56 56" fill="#111"><path d="M6 52V22h14V6h30v46H36v-10h-8v10z"/><g fill="#fff"><rect x="25" y="11" width="5" height="5"/><rect x="36" y="11" width="5" height="5"/><rect x="25" y="21" width="5" height="5"/><rect x="36" y="21" width="5" height="5"/><rect x="25" y="31" width="5" height="5"/><rect x="36" y="31" width="5" height="5"/><rect x="10" y="27" width="5" height="5"/><rect x="10" y="37" width="5" height="5"/></g></svg>
      </div>
      <div class="sector-name">Commercial</div>
    </div>
    <div class="sector" style="left:708px">
      <div class="sector-badge">
        <svg width="56" height="56" viewBox="0 0 56 56" fill="#111"><path d="M4 52V28l12-8v8l12-8v8l12-8V8h8v44z"/><g fill="#fff"><rect x="10" y="36" width="5" height="5"/><rect x="20" y="36" width="5" height="5"/><rect x="30" y="36" width="5" height="5"/><rect x="40" y="36" width="5" height="5"/></g></svg>
      </div>
      <div class="sector-name">Industrial</div>
    </div>
    <div class="sector" style="left:899px">
      <div class="sector-badge">
        <svg width="56" height="56" viewBox="0 0 56 56" fill="#111"><path d="M28 6L3 28h7v22h14V36h8v14h14V28h7z"/></svg>
      </div>
      <div class="sector-name">Homes</div>
    </div>
  </section>

  <footer class="site-footer">
    <div class="item" style="left:220px">Copyright 2014 Brightvale</div>
    <div class="item" style="left:416px">
      <svg width="14" height="14" viewBox="0 0 24 24"><path d="M5 2l4 5-2.5 2.5a13 13 0 0 0 8 8L17 15l5 4-2 3C11 22 2 13 2 4z" fill="#fff"/></svg>
      Phone: 987 604 215
    </div>
    <div class="item" style="left:596px">
      <svg width="15" height="12" viewBox="0 0 24 18"><rect x="1" y="1" width="22" height="16" fill="none" stroke="#fff" stroke-width="2"/><path d="M1 1l11 9 11-9" fill="none" stroke="#fff" stroke-width="2"/></svg>
      info@brightvalena.com
    </div>
    <div class="item" style="left:785px;top:14px">
      <svg width="22" height="18" viewBox="0 0 24 20"><path d="M2 8l10-7 10 7v11H2z" fill="none" stroke="#fff" stroke-width="2"/><path d="M2 8l10 7 10-7" fill="none" stroke="#fff" stroke-width="2"/></svg>
    </div>
    <div class="newsletter">enter your email here</div>
  </footer>
</body>
</html>
```